Marlow Ridge Dental business card

Business card would have following info:

Alden R. Kasprzak, DMD, FAGD
General Dentist
email: office@marlowridgedental.example
phone: 617-490-3867
fax: 617-490-3867
website: marlowridgedental.example

second side would have lines for:

appointment date
appointment time

```html
<!DOCTYPE html>
<html lang="en">
<head>
<meta charset="utf-8">
<title>Marlow Ridge Dental — Business Card</title>
<link href="https://fonts.googleapis.com/css2?family=Lato:wght@400;700;900&display=swap" rel="stylesheet">
<style>
  :root {
    --purple: #713f98;
    --orange: #f3911f;
    --white: #ffffff;
    --ink: #2f2f2f;
    --backdrop: #3b3b3d;
  }
  * { box-sizing: border-box; margin: 0; padding: 0; }
  html, body { width: 1200px; height: 875px; overflow: hidden; }
  body {
    background: var(--backdrop);
    font-family: "Lato", sans-serif;
    display: flex;
    align-items: center;
    justify-content: center;
    gap: 40px;
  }
  .card {
    width: 525px;
    height: 300px;
    border-radius: 18px;
    position: relative;
    overflow: hidden;
  }

  /* Appointment side */
  .card--appointment { background: var(--white); color: var(--purple); padding: 42px 40px 30px; }
  .brand-name {
    text-align: center;
    font-weight: 900;
    font-size: 34px;
    letter-spacing: 0.5px;
    text-transform: uppercase;
    color: var(--purple);
  }
  .appointment-lines { margin-top: 38px; }
  .appointment-row {
    display: flex;
    align-items: baseline;
    font-size: 14px;
    margin-bottom: 18px;
  }
  .appointment-row .label { flex: none; }
  .appointment-row .fill {
    flex: 1;
    border-bottom: 1.5px dotted var(--purple);
    margin: 0 4px;
  }
  .appointment-row .fill--date { flex: 1.3; }
  .appointment-row .fill--time { flex: 1; }
  .appointment-row .meridiem { font-size: 11px; flex: none; }
  .notice {
    margin-top: 16px;
    text-align: center;
    font-size: 11.5px;
    line-height: 1.45;
    color: var(--ink);
  }

  /* Contact side */
  .card--contact {
    background: var(--purple);
    display: flex;
    align-items: center;
    padding: 0 34px;
  }
  .identity { text-align: right; padding-right: 16px; }
  .identity .name {
    color: var(--orange);
    font-weight: 700;
    font-size: 23px;
    text-transform: uppercase;
    white-space: nowrap;
  }
  .identity .credentials { color: var(--orange); font-size: 15px; margin-top: 3px; }
  .identity .role { color: var(--white); font-size: 15px; margin-top: 2px; }
  .divider { width: 1.5px; height: 96px; background: var(--orange); flex: none; }
  .contact-list { list-style: none; padding-left: 16px; }
  .contact-list li {
    display: flex;
    align-items: center;
    gap: 9px;
    color: var(--white);
    font-size: 13px;
    line-height: 1;
    margin: 7px 0;
    white-space: nowrap;
  }
  .contact-list svg { width: 12px; height: 12px; flex: none; fill: var(--orange); }
</style>
</head>
<body>

  <section class="card card--appointment" aria-label="Appointment side">
    <h1 class="brand-name">Marlow Ridge Dental</h1>
    <div class="appointment-lines">
      <div class="appointment-row">
        <span class="label">DATE</span><span class="fill fill--date"></span>
        <span class="label">TIME</span><span class="fill fill--time"></span>
        <span class="meridiem">AM\PM</span>
      </div>
      <div class="appointment-row">
        <span class="label">DATE</span><span class="fill fill--date"></span>
        <span class="label">TIME</span><span class="fill fill--time"></span>
        <span class="meridiem">AM\PM</span>
      </div>
    </div>
    <p class="notice">If you are unable to keep your appointment, please call us to<br>reschedule atleast 48 hours prior to your appointment.</p>
  </section>

  <section class="card card--contact" aria-label="Contact side">
    <div class="identity">
      <p class="name">Alden R. Kasprzak</p>
      <p class="credentials">DMD, FAGD</p>
      <p class="role">General Dentist</p>
    </div>
    <div class="divider"></div>
    <ul class="contact-list">
      <li>
        <svg viewBox="0 0 24 24" aria-label="Phone"><path d="M6.6 10.8a15.5 15.5 0 0 0 6.6 6.6l2.2-2.2c.3-.3.7-.4 1-.2 1.1.4 2.3.6 3.6.6.6 0 1 .4 1 1V20c0 .6-.4 1-1 1A17 17 0 0 1 3 4c0-.6.4-1 1-1h3.5c.6 0 1 .4 1 1 0 1.3.2 2.5.6 3.6.1.3 0 .7-.2 1z"/></svg>
        617-490-3867
      </li>
      <li>
        <svg viewBox="0 0 24 24" aria-label="Fax"><path d="M6 2h10l2 2v5H6zM4 10h16a2 2 0 0 1 2 2v6h-4v4H6v-4H2v-6a2 2 0 0 1 2-2zm4 7v3h8v-3z"/></svg>
        617-490-3867
      </li>
      <li>
        <svg viewBox="0 0 24 24" aria-label="Email"><path d="M2 5h20v14H2zm2 2v.5l8 5.5 8-5.5V7l-8 5.2z"/></svg>
        office@marlowridgedental.example
      </li>
      <li>
        <svg viewBox="0 0 24 24" aria-label="Website"><path d="M12 2a10 10 0 1 0 0 20 10 10 0 0 0 0-20zm0 2c1 0 2.3 2.1 2.8 5H9.2C9.7 6.1 11 4 12 4zM4.3 11h4.7a18 18 0 0 0 0 2H4.3a8 8 0 0 1 0-2zm6.7 0h2a16 16 0 0 1 0 2h-2a16 16 0 0 1 0-2zm4 0h4.7a8 8 0 0 1 0 2H15a18 18 0 0 0 0-2zM9.2 15h5.6c-.5 2.9-1.8 5-2.8 5s-2.3-2.1-2.8-5z"/></svg>
        marlowridgedental.example
      </li>
    </ul>
  </section>

</body>
</html>
```